Can design for new all natural low calorie spiked lemonade

We need a clean but catchy can design for a new spiked lemonade that will be all natural, gluten free and low in calories. Open to any creative ideas ranging from designs such as using a lemonade stand to simple designs such as the example pictures that are uploaded. Looking for a can that just pops out right away on the shelf but also believe less is more as far as simplicity. The beverage is called Brightlow Spiked Lemonade, that features 3 flavors. Traditional Lemonade, Peach Lemonade and lastly Strawberry Lemonade.

Target Market(s)

21-55 years of age. 75% female, 25% male.

Colors

Designer to choose colors to be used in the design.

Requirements
Must have
• The brand name is Brightlow and it is a spiked lemonade so that should be catchy so the consumer knows what it is on first glance. Must say gluten free, all natural, and 150 calories on the front of the can. Would like some type of image on the front middle of the can. There are 3 flavors so the can should blend well with each fruit but not be different cans

```html
<!DOCTYPE html>
<html lang="en">
<head>
<meta charset="utf-8">
<title>Brightlow Spiked Lemonade – Can Wrap</title>
<link href="https://fonts.googleapis.com/css2?family=Oswald:wght@400;500;600;700&display=swap" rel="stylesheet">
<style>
  :root {
    --backdrop: #e4e5e8;
    --label-black: #0d0d0d;
    --label-white: #f4f4f2;
    --rule-grey: #8a8a8a;
    --lemon-bright: #f7ea1c;
    --lemon-pale: #fbf4a0;
    --lime-green: #9cc93a;
    --wash-white: #fdfbe6;
  }
  * { margin: 0; padding: 0; box-sizing: border-box; }
  html, body {
    width: 1200px;
    height: 1200px;
    overflow: hidden;
  }
  body {
    background: var(--backdrop);
    font-family: "Oswald", sans-serif;
    display: flex;
    align-items: center;
    justify-content: center;
  }
  .can-wrap {
    position: relative;
    width: 520px;
    height: 1080px;
    overflow: hidden;
  }
  .citrus-artwork {
    position: absolute;
    inset: 0;
    background:
      radial-gradient(circle at 88% 8%, var(--lime-green) 0 12%, transparent 22%),
      radial-gradient(circle at 10% 6%, var(--wash-white) 0 10%, transparent 20%),
      radial-gradient(circle at 85% 92%, var(--lime-green) 0 6%, transparent 14%),
      radial-gradient(ellipse at 40% 94%, var(--wash-white) 0 14%, transparent 30%),
      linear-gradient(180deg, var(--lemon-bright) 0%, var(--lemon-pale) 45%, var(--lemon-bright) 80%, var(--lemon-pale) 100%);
  }
  .front-label {
    position: absolute;
    left: 35px;
    right: 35px;
    top: 151px;
    height: 832px;
    background: var(--label-black);
    border: 3px solid var(--label-white);
    color: var(--label-white);
    display: flex;
    flex-direction: column;
    align-items: center;
    padding: 48px 26px 40px;
    text-align: center;
  }
  .brand-name {
    font-weight: 500;
    font-size: 80px;
    line-height: 1;
    letter-spacing: 0.09em;
    text-transform: uppercase;
  }
  .product-kind {
    margin-top: 58px;
    font-weight: 500;
    font-size: 80px;
    line-height: 1;
    letter-spacing: 0.2em;
    text-transform: uppercase;
    padding-left: 0.2em;
  }
  .flavour-name {
    margin-top: 56px;
    font-weight: 700;
    font-size: 84px;
    line-height: 1;
    letter-spacing: 0.01em;
    text-transform: uppercase;
  }
  .rule {
    width: 100%;
    height: 2px;
    background: var(--rule-grey);
  }
  .rule-top { margin-top: 34px; }
  .flavour-note {
    margin: 18px 0 20px;
    font-weight: 600;
    font-size: 44px;
    line-height: 1;
    text-transform: uppercase;
  }
  .claims {
    margin-top: 22px;
    font-weight: 500;
    font-size: 21px;
    line-height: 1;
    text-transform: uppercase;
    letter-spacing: 0.01em;
  }
  .volume {
    margin-top: auto;
    font-weight: 600;
    font-size: 46px;
    line-height: 1;
    text-transform: uppercase;
  }
</style>
</head>
<body>
  <main class="can-wrap">
    <div class="citrus-artwork" role="img" aria-label="Watercolour illustration of sliced lemons and limes in bright yellow and green"></div>
    <section class="front-label">
      <h1 class="brand-name">Brightlow</h1>
      <p class="product-kind">Spiked</p>
      <p class="flavour-name">Lemonade</p>
      <div class="rule rule-top"></div>
      <p class="flavour-note">Fresh Lime Juice</p>
      <div class="rule"></div>
      <p class="claims">Gluten Free | All Natural | 150 Calories</p>
      <p class="volume">330ml</p>
    </section>
  </main>
</body>
</html>
```